Business card

We need a business card design for our company based in Auckland , New Zealand called 'Kestrel + Design Ltd'. We provide architectural services. We would like to see designs that use the max. three colours (such as white, black, grey) The final design should communicate financial safety and growth."
Also I will provide our company logo. I would like to the logo to be embeded onto our business card.

Target Market(s)

new residential house, alteration & addition & light commericila design & drafting service

Industry/Entity Type

Architecture

Contact Information for Business Card

Company name: kestrel + design Ltd.
Name: Mark Telford
Job title: architectural designer & Design RQC
email address: mark@kdstudio.co.nz
mobile number: 02 5319 6620
web site: www.kdstudio.co.nz

Requirements
Must have
• My project must have..
• - embeded logo (attached company logo)
• I don't have a bigger version for our company logo, but I have one old one, so you can remove the word from it)
• - insert the attached small PDGQ logo & RQC logo
• - creative, simple and clear business card.
• - Max. three colours
Nice to have
• - Here are the samples I would like to share with you: http://www.velmorindex.com/blog/minimalistic-business-card-designs/
• I would like to have my business card like one of the creation.
Should not have
• TBA

```html
<!DOCTYPE html>
<html lang="en">
<head>
<meta charset="utf-8">
<title>Mark Telford – Business Card</title>
<link rel="stylesheet" href="https://fonts.googleapis.com/css2?family=Open+Sans:wght@400;600;700;800&family=PT+Sans+Narrow&display=swap">
<style>
  :root {
    --backdrop: #3b3b3b;
    --paper: #ffffff;
    --ink: #111111;
    --muted: #8a9290;
    --night: #000000;
    --snow: #ffffff;
  }
  * { box-sizing: border-box; margin: 0; padding: 0; }
  html, body {
    width: 1105px; height: 1200px; overflow: hidden;
    background: var(--backdrop);
    font-family: "Open Sans", Arial, sans-serif;
  }
  .card {
    position: absolute; left: 193px; width: 720px; height: 410px;
  }
  .card--front { top: 167px; background: var(--paper); color: var(--ink); }
  .card--back { top: 623px; background: var(--night); color: var(--snow); }

  .brand-mark {
    position: absolute; left: 87px; top: 99px; width: 220px; height: 220px;
    display: flex; flex-direction: column; align-items: center; justify-content: center;
    gap: 12px;
  }
  .brand-mark__dot {
    width: 34px; height: 34px; border-radius: 50%; background: var(--ink);
  }
  .brand-mark__name {
    font-size: 24px; font-weight: 600; color: var(--ink); letter-spacing: 0.5px;
  }

  .divider { position: absolute; width: 1px; }
  .card--front .divider { left: 334px; top: 109px; height: 207px; background: #cfcfcf; }
  .card--back .divider { left: 325px; top: 95px; height: 235px; background: var(--snow); }

  .details { position: absolute; left: 357px; top: 107px; }
  .details__name { font-size: 25px; font-weight: 700; line-height: 32px; }
  .details__role {
    font-family: "PT Sans Narrow", Arial, sans-serif;
    font-size: 19px; color: var(--muted); line-height: 24px;
  }
  .details__company { margin-top: 20px; font-size: 18px; line-height: 24px; }
  .contact { list-style: none; margin-top: 12px; }
  .contact li {
    display: flex; align-items: center; gap: 10px;
    font-size: 18px; line-height: 27.5px; color: #333;
  }
  .contact svg { width: 16px; height: 16px; flex: none; }

  .badge {
    position: absolute; left: 112px; top: 87px; width: 182px; height: 182px;
    border-radius: 50%; background: var(--snow);
    display: flex; align-items: center; justify-content: center;
  }
  .badge__core { width: 132px; height: 132px; border-radius: 50%; background: var(--night); }

  .partner-name {
    position: absolute; left: 345px; top: 128px;
    font-size: 104px; font-weight: 800; line-height: 1; letter-spacing: -3px;
    color: var(--snow);
  }
  .back-web {
    position: absolute; left: 0; right: 0; top: 346px; text-align: center;
    font-size: 19px; color: var(--snow);
  }
</style>
</head>
<body>
  <section class="card card--front">
    <div class="brand-mark">
      <span class="brand-mark__dot"></span>
      <span class="brand-mark__name">kestrel + design</span>
    </div>
    <span class="divider"></span>
    <div class="details">
      <h1 class="details__name">Mark Telford</h1>
      <p class="details__role">architectural designer &amp; Design RQC</p>
      <p class="details__company">kestrel + design Ltd.</p>
      <ul class="contact">
        <li>
          <svg viewBox="0 0 16 16" aria-hidden="true"><rect x="4" y="1" width="8" height="14" rx="1.5" fill="none" stroke="#111" stroke-width="1.6"/><rect x="6.5" y="12" width="3" height="1.2" fill="#111"/></svg>
          02 5319 6620
        </li>
        <li>
          <svg viewBox="0 0 16 16" aria-hidden="true"><rect x="1.5" y="4" width="13" height="9" fill="#111"/><path d="M1.5 4 L8 9 L14.5 4" fill="none" stroke="#fff" stroke-width="1.2"/></svg>
          mark@kdstudio.co.nz
        </li>
        <li>
          <svg viewBox="0 0 16 16" aria-hidden="true"><circle cx="8" cy="8" r="6.5" fill="#111"/><path d="M4 6 Q7 4 8 7 T12 10" fill="none" stroke="#fff" stroke-width="1.2"/></svg>
          www.kdstudio.co.nz
        </li>
      </ul>
    </div>
  </section>

  <section class="card card--back">
    <div class="badge" role="img" aria-label="Registered practitioner certification badge">
      <span class="badge__core"></span>
    </div>
    <span class="divider"></span>
    <p class="partner-name">PDGQ</p>
    <p class="back-web">www.kdstudio.co.nz</p>
  </section>
</body>
</html>
```